Vantrell Law Letterhead

We need a new letterhead design for a Law Firm. The address for the law firm is 4817 Larkspur Boulevard, Suite 250, Houston, Texas 77342. Phone Number: 832-619-3057; Fax Number: 832-407-1694. The logo is uploaded to the project.

```html
<!DOCTYPE html>
<html lang="en">
<head>
<meta charset="utf-8">
<title>Vantrell Law Letterhead</title>
<link rel="stylesheet" href="https://fonts.googleapis.com/css2?family=Roboto:wght@300;400&family=Open+Sans:wght@400&family=Pinyon+Script&display=swap">
<style>
  :root {
    --navy: #0f1f4d;
    --red: #c3182b;
    --paper: #f1f1f3;
    --backdrop: #e6e6e8;
    --ink: #222226;
    --footer-ink: #5a5c66;
  }
  * { margin: 0; padding: 0; box-sizing: border-box; }
  html, body {
    width: 1200px; height: 1012px; overflow: hidden;
    background: var(--backdrop);
  }
  .letterhead {
    position: absolute; left: 246px; top: 0;
    width: 708px; height: 1012px;
    background: var(--paper);
    overflow: hidden;
    font-family: "Roboto", Arial, sans-serif;
    font-weight: 300;
    color: var(--ink);
  }
  .side-band {
    position: absolute; left: 0; top: 0;
    width: 72px; height: 1012px;
    background: linear-gradient(90deg, var(--navy) 0%, var(--navy) 70%, #4a2347 100%);
  }
  .brand {
    position: absolute; right: 75px; top: 58px;
    display: flex; align-items: center; gap: 10px;
  }
  .brand-dot { width: 14px; height: 14px; border-radius: 50%; background: var(--red); }
  .brand-name {
    font-family: "Roboto", Arial, sans-serif; font-weight: 400;
    font-size: 28px; color: var(--navy); letter-spacing: 0.5px;
  }
  .letter-body {
    position: absolute; left: 111px; top: 194px; width: 522px;
    font-size: 12px; line-height: 16.8px;
  }
  .date { margin-bottom: 17px; }
  .recipient { margin-bottom: 33px; }
  .salutation { margin-bottom: 17px; }
  .letter-body p.para { text-align: justify; margin-bottom: 17px; }
  .closing { margin-top: 33px; }
  .signature {
    font-family: "Pinyon Script", cursive;
    font-size: 23px; line-height: 30px; margin-top: 4px;
  }
  .footer {
    position: absolute; left: 111px; top: 920px;
    display: flex; font-family: "Open Sans", Arial, sans-serif;
    font-size: 12.3px; line-height: 14.6px; color: var(--footer-ink);
  }
  .footer-address { font-style: normal; padding-right: 14px; border-right: 1px solid #8a8c95; }
  .footer-contact { padding-left: 15px; }
  .footer-contact li { list-style: none; display: flex; align-items: center; gap: 6px; }
  .footer-contact svg { width: 10px; height: 10px; fill: var(--navy); }
</style>
</head>
<body>
<main class="letterhead">
  <div class="side-band" role="img" aria-label="Decorative navy and red side band"></div>

  <header class="brand">
    <span class="brand-dot"></span>
    <span class="brand-name">Vantrell Law</span>
  </header>

  <section class="letter-body">
    <p class="date">01 January 2050</p>
    <p class="recipient">Company (Pvt) Ltd.<br>PO Box 3355 Mainville St<br>Sample City Country 3355</p>
    <p class="salutation">Dear Daniel Ashworth,</p>
    <p class="para">Lorem ipsum dolor sit amet, consectetuer adipiscing elit, sed diam nonummy nibh euismod tincidunt ut laoreet dolore magna aliquam erat volutpat. Ut wisi enim ad minim veniam, quis nostrud exerci tation ullamcorper suscipit lobortis nisl ut aliquip ex ea commodo consequat. Duis dolore te feugait nulla facilisi. Nam liber tempor cum soluta nobis eleifend option congue nihil imperdiet doming id quod mazim placerat facer possim assum. Lorem ipsum dolor sit amet, consectetuer adipiscing elit, sed diam nonummy nibh euismod tincidunt ut laoreet dolore magna aliquam erat volutpat. Ut wisi enim ad minim veniam, quis nostrud exerci tation ullamcorper suscipit lobortis nisl ut aliquip ex ea commodo consequat.</p>
    <p class="para">Consectetuer adipiscing elit, sed diam nonummy nibh euismod tincidunt ut laoreet dolore magna aliquam erat volutpat. Ut wisi enim ad minim veniam, quis nostrud exerci tation ullamcorper suscipit lobortis nisl ut aliquip ex ea commodo consequat. Consectetuer adipiscing elit, sed diam nonummy nibh euismod tincidunt ut laoreet dolore magna aliquam erat volutpat. Ut wisi enim ad minim veniam, quis nostrud exerci tation ullamcorper suscipit lobortis nisl ut aliquip ex ea commodo consequat.</p>
    <p class="para">Consectetuer adipiscing elit, sed diam nonummy nibh euismod tincidunt ut laoreet dolore magna aliquam erat volutpat. Ut wisi enim ad minim veniam, quis nostrud exerci tation ullamcorper suscipit lobortis nisl ut aliquip ex ea commodo consequat. Consectetuer adipiscing elit, sed diam nonummy nibh euismod tincidunt ut laoreet dolore magna aliquam erat volutpat. Ut wisi enim ad minim veniam, quis nostrud exerci tation ullamcorper suscipit lobortis nisl ut aliquip ex ea commodo consequat.</p>
    <p class="closing">Sincerely Yours</p>
    <p class="signature">Martin Olsen</p>
  </section>

  <footer class="footer">
    <address class="footer-address">
      Vantrell Law<br>4817 Larkspur Boulevard<br>Suite 250<br>Houston, Texas 77342
    </address>
    <ul class="footer-contact">
      <li><svg viewBox="0 0 10 10"><path d="M2 0.5 L3.6 2.6 L2.7 3.6 C3.3 4.9 4.9 6.6 6.3 7.2 L7.3 6.3 L9.5 7.9 L8.4 9.5 C4.6 9.3 0.7 5.4 0.5 1.6 Z"/></svg>832-619-3057</li>
      <li><svg viewBox="0 0 10 10"><path d="M2.5 0.5 H7.5 V3 H2.5 Z M0.5 3.5 H9.5 V7.5 H8 V6 H2 V7.5 H0.5 Z M2.5 6.5 H7.5 V9.5 H2.5 Z"/></svg>832-407-1694</li>
      <li><svg viewBox="0 0 10 10"><path d="M0.5 2 H9.5 V2.6 L5 5.6 L0.5 2.6 Z M0.5 3.6 L5 6.6 L9.5 3.6 V8 H0.5 Z"/></svg>contact@vantrellinjury.com</li>
      <li><svg viewBox="0 0 10 10"><circle cx="5" cy="5" r="4.2" fill="none" stroke="var(--navy)" stroke-width="1"/><ellipse cx="5" cy="5" rx="1.8" ry="4.2" fill="none" stroke="var(--navy)" stroke-width="0.9"/><path d="M0.8 5 H9.2" stroke="var(--navy)" stroke-width="0.9"/></svg>www.vantrellinjury.com</li>
    </ul>
  </footer>
</main>
</body>
</html>
```